Portfolio required for virtual assistant seeking new clients

I require an editable Word template that can be sent to clients. This is a new business venture I am undertaking - working as a virtual assistant (administration work). I will need to find my own clients so would like Wow factor. Target group will be small businesses/legal industry so needs to look professional.
The portfolio will need to note information about me, why hire me, my skill set and credentials. May add testimonials too. I have attached a draft of the amount of text required - still working on this.
I will upload my logo and business card design. I do like consistency.
Colours used Pantone 2745 C and 272 C. Open to other colours but would like to see the main colours of logo incorporated. Images welcome. May insert an image of myself at some stage so please allow for a spot for this photo.
The portfolio will need to be converted to pdf to send by email as well as printable.
Updates

Automatically set for 24 hours apologies did not see this. Now amended

```html
<!DOCTYPE html>
<html lang="en">
<head>
<meta charset="utf-8">
<title>Mara Quell – Virtual Assistant Portfolio</title>
<link rel="stylesheet" href="https://fonts.googleapis.com/css2?family=Jost:wght@400;600;700&family=Montserrat:wght@500;600&display=swap">
<style>
  :root {
    --navy: #2e3478;
    --periwinkle: #6b78c8;
    --ink: #1e1e24;
    --page: #ffffff;
    --backdrop: #b3b3b3;
    --rule: #7c86c9;
  }
  * { box-sizing: border-box; margin: 0; padding: 0; }
  html, body { width: 1200px; height: 900px; overflow: hidden; }
  body { background: var(--backdrop); font-family: "Jost", sans-serif; color: var(--ink); position: relative; }

  .page { position: absolute; top: 153px; width: 420px; height: 594px; background: var(--page); overflow: hidden; }
  .page--about { left: 157px; }
  .page--services { left: 623px; }

  .brand { position: absolute; top: 26px; left: 0; width: 100%; text-align: center; color: var(--navy); }
  .brand__dot { display: block; width: 34px; height: 34px; border-radius: 50%; background: var(--periwinkle); margin: 0 auto 16px; }
  .brand__name { font-family: "Montserrat", sans-serif; font-weight: 600; font-size: 21px; letter-spacing: 5.5px; line-height: 1; padding-left: 5px; }
  .brand__role { font-family: "Montserrat", sans-serif; font-weight: 500; font-size: 11.3px; letter-spacing: 3.9px; margin-top: 7px; padding-left: 4px; }

  .section-head { position: absolute; left: 29px; width: 361px; height: 14px; }
  .section-head__marker { position: absolute; left: 0; top: -5px; width: 19px; height: 19px; border-radius: 50%; background: var(--periwinkle); }
  .section-head__title { position: absolute; left: 52px; top: -4px; font-weight: 700; font-size: 10.5px; color: var(--navy); letter-spacing: .2px; }
  .section-head__rule { position: absolute; left: 23px; right: 0; top: 10px; height: 1px; background: var(--rule); }

  .copy { position: absolute; left: 81px; width: 310px; font-size: 9px; line-height: 10.15px; }
  .copy p + p { margin-top: 8px; }
  .copy--about { top: 172px; }
  .portrait { float: left; width: 130px; height: 130px; margin: -16px 4px 0 -45px;
    background: radial-gradient(circle at 50% 50%, #c2a38e 0, #8a7f86 28px, #4c5a72 46px, transparent 47px);
    shape-outside: circle(65px at 65px 65px) border-box; }
  .copy--hire { top: 406px; }

  .banner { position: absolute; top: 0; left: 0; width: 100%; height: 119px;
    background: linear-gradient(110deg, #6e3b32 0%, #8c5a50 40%, #a77466 70%, #7a4536 100%); }

  .services { position: absolute; top: 172px; font-size: 8.8px; line-height: 10.1px; }
  .services--left { left: 82px; width: 160px; }
  .services--right { left: 245px; width: 150px; }
  .services h3 { font-size: 8.8px; font-weight: 700; color: var(--ink); }
  .services ul { list-style: none; margin-bottom: 10px; }
  .services li { position: relative; padding-left: 10px; }
  .services li::before { content: ""; position: absolute; left: 1px; top: 4px; width: 2.8px; height: 2.8px; border-radius: 50%; background: var(--ink); }

  .credentials { position: absolute; left: 82px; top: 458px; font-size: 8.8px; line-height: 10.4px; }

  .contact-bar { position: absolute; left: 0; bottom: 0; width: 100%; height: 30px; background: var(--navy); color: #fff; font-size: 8.5px; }
  .contact-bar span { position: absolute; top: 8px; }
  .contact-bar .email { left: 29px; }
  .contact-bar .sep1 { left: 141px; }
  .contact-bar .phone { left: 182px; }
  .contact-bar .sep2 { left: 273px; }
  .contact-bar .abn { left: 314px; }
</style>
</head>
<body>

<section class="page page--about">
  <header class="brand">
    <span class="brand__dot"></span>
    <div class="brand__name">MARA QUELL</div>
    <div class="brand__role">VIRTUAL ASSISTANT</div>
  </header>

  <div class="section-head" style="top:152px">
    <span class="section-head__marker"></span>
    <span class="section-head__rule"></span>
    <h2 class="section-head__title">ABOUT ME</h2>
  </div>

  <div class="copy copy--about">
    <div class="portrait" role="img" aria-label="Portrait photo of the virtual assistant"></div>
    <p>Hello, I'm Mara Quell, a mother, coffee lover, and a passion for travel. I enjoy organisation and making life easy. With over 15 years of experience in the legal field, I have gained valuable experience whilst at the same time, perfecting my skills.</p>
    <p>Throughout my journey in the legal profession, I have held various roles, each contributing to my growth and expertise. Starting as a Rounds Clerk, I quickly advanced to the role of Administrative Assistant in the area of Litigation which involved leading a team of administration assistants focused on supporting legal professionals and litigation processes. This role was invaluable in that it taught me the importance of organisation, time management, attention to detail and multitasking.</p>
    <p>I then transitioned into Debt Recovery, where I thrived as a Paralegal. In this role, I took on the responsibility of managing my own caseload and providing comprehensive legal support independently. Attention to detail, meticulous research and effective communication became second nature. This allowed me to achieve successful resolutions while maintaining the utmost organization and professionalism.</p>
  </div>

  <div class="section-head" style="top:387px">
    <span class="section-head__marker"></span>
    <span class="section-head__rule"></span>
    <h2 class="section-head__title">WHY HIRE ME?</h2>
  </div>

  <div class="copy copy--hire">
    <p>A virtual assistant is an affordable alternative to hiring on-site administration support. Hire me for a once-off task or on a regular basis. I'm here to help you so get more time back in your day so you can focus on more important tasks. I want to save you time, as who has enough of that these days!</p>
    <p>I am known for my reliability, determination, ability to work diligently in fast-paced environments as well as delivering results. I take pride in my meticulous approach to the tasks I undertake. I adapt well to new technology.</p>
    <p>I am excited to embrace new opportunities that allow me to showcase my skill set expertise, provide dedicated support to professionals and that may involve my legal expertise. I am committed to making a positive impact wherever I go, bringing efficiency and structure.</p>
  </div>

  <footer class="contact-bar">
    <span class="email">mara@mqva.net.au</span><span class="sep1">|</span>
    <span class="phone">0491 570 118</span><span class="sep2">|</span>
    <span class="abn">ABN: 12 345 678 901</span>
  </footer>
</section>

<section class="page page--services">
  <div class="banner" role="img" aria-label="Photo of hands typing on a laptop beside a phone and notebook on a desk"></div>

  <div class="section-head" style="top:152px">
    <span class="section-head__marker"></span>
    <span class="section-head__rule"></span>
    <h2 class="section-head__title">WHAT CAN I DO FOR YOU?</h2>
  </div>

  <div class="services services--left">
    <h3>General administration support</h3>
    <ul>
      <li>Document preparation including editing and formatting</li>
      <li>Spreadsheets</li>
      <li>Client correspondence</li>
      <li>Customer service / telephone calls</li>
      <li>Invoicing</li>
      <li>Bulk mail outs</li>
      <li>Data entry</li>
      <li>Database and records management</li>
    </ul>
    <h3>Email management</h3>
    <ul>
      <li>Categorize and prepare sub folders</li>
      <li>Prioritize emails</li>
      <li>Send email correspondence</li>
    </ul>
    <h3>Calendar &amp; diary management</h3>
    <ul>
      <li>Assist with scheduling appointments and meetings</li>
      <li>Scheduling reminders</li>
    </ul>
    <h3>Travel arrangements</h3>
    <ul>
      <li>Assist with booking intrastate/interstate travel</li>
      <li>Assist with car hire and accommodation</li>
    </ul>
  </div>

  <div class="services services--right">
    <h3>Software</h3>
    <ul>
      <li>Quillbook 365</li>
      <li>Ledgerly Practice</li>
      <li>Docketa</li>
    </ul>
    <h3>Debt Collection</h3>
    <ul>
      <li>Assist with sending out overdue statements</li>
      <li>Issue demand letters</li>
      <li>Issue Claims and enforcement action in the Magistrates Court of Westmere</li>
      <li>Negotiating payment arrangements</li>
      <li>Knowledge with Courtwell portal</li>
    </ul>
    <h3>Other</h3>
    <ul>
      <li>Online research</li>
      <li>Event coordination</li>
    </ul>
    <h3>Legal</h3>
    <ul>
      <li>Courtwell portal</li>
      <li>Preparing Court documents</li>
      <li>Filing Court Documents</li>
    </ul>
  </div>

  <div class="section-head" style="top:440px">
    <span class="section-head__marker"></span>
    <span class="section-head__rule"></span>
    <h2 class="section-head__title">CREDENTIALS</h2>
  </div>

  <div class="credentials">
    <p>Certificate IV in Business (Legal Services)</p>
    <p>Certificate III of Business Administration</p>
    <p>Certificate II in Business</p>
  </div>

  <footer class="contact-bar">
    <span class="email">mara@mqva.net.au</span><span class="sep1">|</span>
    <span class="phone">0491 570 118</span><span class="sep2">|</span>
    <span class="abn">ABN: 12 345 678 901</span>
  </footer>
</section>

</body>
</html>
```